FULL Stationary & Business Cards for Innovative Software Company
Stationary/Business Card/Email Signatures
FULL Stationary & Business Cards for Innovative Software Company - Software
Creative Brief
Professional
Miles Tenvard
Managing Partner
412 Harrow Bend Road Suite 309, North Annex Mississauga, ON L4T 2K8
milest@quelvoworks.example
www.quelvoworks.example
restwzeasy restwzeasy
Please submit all of your final stationary designs. We are making a decision soon.
sevensky sevensky
Please tell which design no we use to make stationary package??
Can you please submit full stationary for the designs that were evaluated with stars?
Watermark logo on back of the card is very interesting.
The cards must show all of the provided contact information. Some of the designs only show the telephone without the address.
The front of the card should be easy to read, but also be interesting. All white on the front is little boring.
We like the designs with the back of the card in red instead of blue.
We are not very interested in a border on the front of the card.
Check #140, also its a veiled contest, no one can see other designs, so kindly send a comment/feedback through private messeging service of panelhive, thanks! regards
design #132, looks better, but little plain on the front page.
We like the designs with some creative content on the front, but not too intrusive. We are not very interested in all white front of the card - we feel that is too plan. At the same time, the design should complement the information, not distract from it. Please continue to submit your designs. Innovative, fresh, professional are some of the characteristics we are trying to communicate.
On the folder designs, please be little more creative. A lot of them look plain. We are trying to communicate that we are an interesting, innovative, leading edge software company.
#81, the content is all in the centre of the card. Please try to spread the content around the card.
We like the back designs with only the logo instead of having the contact information.
We like the designs that make use of the space instead of all of the text being grouped in one specific area of the card leaving 1/2 of the business card space obviously empty. It should be easy for someone to quickly scan the card and see the name, address, and contact information instead of having to search for it.
We like the red back of the card better than the blue.
Please use the Quelvo logo without the "TM" (trademark).
Xpert Xpert
Sir, can you give some star rating first then we move towards stationery to the rated designs. Thanks
Thank you for the designs, but please keep in mind that the request is for all stationary including 2 sided business cards, letterhead, envelopes, email signature, and portfolio.

```html
<!DOCTYPE html>
<html lang="en">
<head>
<meta charset="utf-8">
<title>Quelvo Business Card</title>
<link rel="stylesheet" href="https://fonts.googleapis.com/css2?family=Open+Sans:wght@400;600&display=swap">
<style>
  :root {
    --backdrop: #d9d8d5;
    --card: #f7f7f5;
    --brand-red: #c1272d;
    --ink: #3a3a3a;
    --paper-white: #ffffff;
  }
  html, body {
    margin: 0;
    padding: 0;
    width: 1200px;
    height: 940px;
    overflow: hidden;
    background: var(--backdrop);
    font-family: "Open Sans", Arial, sans-serif;
  }
  .business-card {
    position: absolute;
    left: 150px;
    top: 210px;
    width: 900px;
    height: 520px;
    background: var(--card);
    border-radius: 36px;
    overflow: hidden;
    box-shadow: 0 4px 14px rgba(0,0,0,0.12);
  }
  .brand-name {
    position: absolute;
    left: 80px;
    top: 48px;
    margin: 0;
    font-size: 92px;
    font-weight: 600;
    letter-spacing: 2px;
    line-height: 1;
    color: var(--brand-red);
  }
  .name-band {
    position: absolute;
    left: 0;
    top: 190px;
    width: 100%;
  }
  .band-rule {
    height: 6px;
    background: var(--brand-red);
  }
  .band-body {
    margin: 8px 0;
    height: 120px;
    background: var(--brand-red);
    color: var(--paper-white);
    padding-left: 80px;
    box-sizing: border-box;
    display: flex;
    flex-direction: column;
    justify-content: center;
  }
  .person-name {
    margin: 0;
    font-size: 40px;
    font-weight: 400;
    text-transform: uppercase;
    letter-spacing: 1px;
    line-height: 1.15;
  }
  .person-title {
    margin: 4px 0 0;
    font-size: 26px;
    font-weight: 400;
    line-height: 1.2;
  }
  .contact-list {
    position: absolute;
    left: 80px;
    top: 366px;
    margin: 0;
    padding: 0;
    list-style: none;
    color: var(--ink);
    font-size: 20px;
    line-height: 1.45;
  }
</style>
</head>
<body>
  <article class="business-card">
    <h1 class="brand-name">Quelvo</h1>
    <div class="name-band">
      <div class="band-rule"></div>
      <div class="band-body">
        <p class="person-name">Miles Tenvard</p>
        <p class="person-title">Managing Director</p>
      </div>
      <div class="band-rule"></div>
    </div>
    <ul class="contact-list">
      <li>412 Harrow Bend Road Suite 309, North Annex Mississauga, ON L4T 2K8</li>
      <li>014 552 0937</li>
      <li>milest@quelvoworks.example</li>
      <li>www.quelvoworks.example</li>
    </ul>
  </article>
</body>
</html>
```